Creative Advertisements for Magazine

Require one (1) ad created for a full page, 1/3 page, 2/3 page size.

Video Monitoring Solution - we are currently creating an explainer video of this offering and I have attached the document for the video monitoring script to help you understand what we are selling. Please also watch the 1 minute overview of who we are and what we do at https://videohost.example/Kq7PzLm2Vd . The creative magazine ad should include an image of a monitoring station (could be animated) watching a crime occurring through security cameras or something like that. You will need to rewrite the below items to be effective and have a call to action.

Our monitoring station reacts immediately to emergency events or crimes in progress by talking to the intruder and/or calling the police or your contact list. Your site management can also login anytime and view the site from their phone or PC.

The security cameras, 24/7 video storage and audible speakers can be purchased or rented from The Lookwell Depot. We install, program and monitor the system. Prices start at $175/month. Reduce Crime, Improve Site Management.

we will need our four vertical logos (as shown in the attached file and brochure) to be in the ad along with our phone numbers shown in the business card and email sales@lookdepot.example and website www.lookdepot.example. I'm hoping the general feel of the ad can match our existing feel of our brochure and attached post card.

```html
<!DOCTYPE html>
<html lang="en">
<head>
<meta charset="utf-8">
<title>The Lookwell Depot – Magazine Page Ad</title>
<link rel="stylesheet" href="https://fonts.googleapis.com/css2?family=Questrial&family=Tinos:ital,wght@0,400;1,400&family=Oswald:wght@500&display=swap">
<style>
  :root {
    --backdrop: #4a4b4d;
    --paper: #ffffff;
    --ink: #1d1d1f;
    --gold: #d9a21b;
    --rust: #b8401f;
    --quote-brown: #8a3a1a;
    --muted: #8a8a8a;
    --navy: #0f1f3d;
    --orange: #e8491d;
    --white: #ffffff;
  }
  * { box-sizing: border-box; margin: 0; padding: 0; }
  html, body { width: 1200px; height: 862px; overflow: hidden; }
  body { background: var(--backdrop); font-family: "Questrial", sans-serif; }

  .page {
    position: absolute; left: 270px; top: 0;
    width: 660px; height: 862px;
    background: var(--paper);
    overflow: hidden;
  }

  /* Editorial top */
  .editorial { position: absolute; inset: 0 0 auto 0; height: 360px; padding: 28px 34px 0; }
  .dots { display: flex; gap: 4px; margin-bottom: 4px; }
  .dots span { width: 9px; height: 9px; border-radius: 50%; background: var(--rust); }
  .issue-date { position: absolute; right: 34px; top: 70px; color: var(--muted); font-size: 15px; letter-spacing: .5px; }
  .page-heading { font-weight: 400; font-size: 56px; line-height: 1; letter-spacing: 1px; }
  .page-heading .lead { color: var(--gold); }
  .page-heading .rest { color: var(--rust); }
  .page-subheading { font-size: 40px; color: var(--ink); margin: 6px 0 0 150px; letter-spacing: 1px; }

  .columns { display: flex; gap: 24px; margin-top: 16px; }
  .pull-quote {
    position: relative; width: 150px; flex: none;
    font-family: "Tinos", serif; font-style: italic; color: var(--quote-brown);
    font-size: 17px; line-height: 1.35; text-align: right; padding: 6px 4px 0 18px;
  }
  .pull-quote::before, .pull-quote::after {
    position: absolute; font-family: "Tinos", serif; font-size: 72px; color: var(--gold); opacity: .55; font-style: normal; line-height: 1;
  }
  .pull-quote::before { content: "\201C"; left: 0; top: -8px; }
  .pull-quote::after { content: "\201D"; right: 0; bottom: -42px; }
  .body-copy { font-family: "Tinos", serif; font-size: 12.5px; line-height: 1.32; color: var(--ink); text-align: justify; }
  .body-copy .drop-cap { float: left; font-size: 40px; line-height: .9; color: var(--rust); margin: 2px 6px 0 0; }
  .body-copy p + p { margin-top: 4px; }
  .tail-line { font-family: "Tinos", serif; font-size: 12px; color: var(--ink); margin-top: 6px; }

  /* Advertisement */
  .ad { position: absolute; left: 0; right: 0; bottom: 0; height: 520px; }
  .ad-bg { position: absolute; inset: 0; }
  .brand { position: absolute; left: 40px; top: 50px; display: flex; align-items: center; gap: 10px; color: var(--white); }
  .brand-mark { width: 16px; height: 16px; background: var(--white); }
  .brand-name { font-family: "Oswald", sans-serif; font-weight: 500; font-size: 26px; letter-spacing: 1px; text-transform: uppercase; }

  .crowd-art {
    position: absolute; left: 40px; top: 108px; width: 460px; height: 150px;
    background: linear-gradient(90deg, #ffffff 0 82%, var(--orange) 82% 90%, #ffffff 90%);
    opacity: .9; border-radius: 4px;
  }
  .services { position: absolute; left: 36px; top: 278px; display: flex; gap: 22px; }
  .service { display: flex; flex-direction: column; align-items: center; gap: 6px; color: var(--white); font-family: "Oswald", sans-serif; font-size: 13px; }
  .service svg { width: 46px; height: 46px; }

  .tagline { position: absolute; left: 40px; top: 360px; line-height: 1; }
  .tagline .hot { color: var(--orange); font-size: 32px; letter-spacing: 1px; }
  .tagline .cool { color: var(--white); font-size: 30px; letter-spacing: 1px; margin-top: 4px; }

  .monitor-art {
    position: absolute; right: 30px; top: 320px; width: 220px; height: 140px;
    background: linear-gradient(135deg, #2a3a4a, #7a8c98 50%, #3a2a30);
    border: 6px solid #111; border-radius: 6px;
  }

  .contact-bar {
    position: absolute; left: 0; right: 0; bottom: 0; height: 42px;
    background: var(--orange); color: var(--white);
    display: flex; align-items: center; justify-content: space-around; font-size: 16px;
  }
  .contact { display: flex; align-items: center; gap: 7px; }
  .contact svg { width: 15px; height: 15px; }
</style>
</head>
<body>
<main class="page">
  <section class="editorial">
    <div class="dots"><span></span><span></span></div>
    <p class="issue-date">April 2013</p>
    <h1 class="page-heading"><span class="lead">Page</span> <span class="rest">heading</span></h1>
    <p class="page-subheading">with Description</p>
    <div class="columns">
      <blockquote class="pull-quote">Lorem ipsum dol orsit amet, consect etur adipiscing elit. Donec consec­tetur.</blockquote>
      <div class="body-copy">
        <p><span class="drop-cap">A</span>enean arcu leo, volutpat sed dapibus in, pharetra nec risus. Curabitur nec felis leo, at interdum nunc. Nunc dictum lobortis ligula ut euismod. Class aptent taciti sociosqu ad litora torquent per conubia per inceptos himenaeos. Aliquam at urna vitae elit accumsan viverra. In sodales dolor posuere tellus euismod eu suscipit velit pulvinar. Vestibulum bibendum, ipsum nec condimentum placerat, sem justo adipiscing augue, elementum gravida ante dolor ut nulla. Pellentesque pharetra luctus mi, vel posuere nisl lacinia vestibulum. Donec tortor leo, porta sit amet accumsan ac, commodo id enim. Nam pharetra varius sapien, eget aliquam mi mattis at. Mauris sit amet sem orci, quis vulputate eros. Donec ac nunc dolor. Aliquam et lectus enim tesque pharetra luctus mi. Vestibulum bibendum, ipsum nec condimentum placerat, sem justo adipiscing augue, elementum gravida.</p>
        <p class="tail-line">In aliquet velit arcu. Morbi sit amet &nbsp; aliquet velit arcu. Morbi sit amet &nbsp; In aliquet velit arcu. Morbi sit amet</p>
      </div>
    </div>
  </section>

  <section class="ad" aria-label="Advertisement: The Lookwell Depot">
    <svg class="ad-bg" viewBox="0 0 660 520" preserveAspectRatio="none" aria-hidden="true">
      <path d="M0 0 Q330 20 660 70 L660 520 L0 520 Z" fill="var(--navy)"/>
    </svg>
    <div class="brand"><span class="brand-mark"></span><span class="brand-name">The Lookwell Depot</span></div>
    <div class="crowd-art" role="img" aria-label="Illustration: a row of white person figures with one highlighted in orange"></div>

    <ul class="services" role="list">
      <li class="service">
        <svg viewBox="0 0 46 46"><circle cx="23" cy="23" r="21" fill="none" stroke="#fff" stroke-width="2"/><rect x="13" y="18" width="16" height="10" rx="2" fill="#fff"/><path d="M29 21l6-3v10l-6-3z" fill="#fff"/></svg>Cameras
      </li>
      <li class="service">
        <svg viewBox="0 0 46 46"><circle cx="23" cy="23" r="21" fill="none" stroke="#fff" stroke-width="2"/><circle cx="17" cy="17" r="5" fill="none" stroke="#fff" stroke-width="2.5"/><path d="M21 21l11 11M28 28l3-3M31 31l3-3" stroke="#fff" stroke-width="2.5"/></svg>Access
      </li>
      <li class="service">
        <svg viewBox="0 0 46 46"><circle cx="23" cy="23" r="21" fill="none" stroke="#fff" stroke-width="2"/><rect x="14" y="12" width="18" height="22" rx="2" fill="none" stroke="#fff" stroke-width="2"/><rect x="17" y="15" width="12" height="5" fill="#fff"/><path d="M18 24h2M22 24h2M26 24h2M18 28h2M22 28h2M26 28h2" stroke="#fff" stroke-width="2"/></svg>Alarm
      </li>
      <li class="service">
        <svg viewBox="0 0 46 46"><circle cx="23" cy="23" r="21" fill="none" stroke="#fff" stroke-width="2"/><path d="M15 16v10M19 14v12M23 14v12M27 14v12M31 16v10" stroke="#fff" stroke-width="2"/><path d="M13 30h20" stroke="#fff" stroke-width="2"/></svg>Intercom
      </li>
    </ul>

    <div class="tagline">
      <p class="hot">SEE EVERYTHING</p>
      <p class="cool">FROM ANYWHERE</p>
    </div>

    <div class="monitor-art" role="img" aria-label="Photo: tablet and phone screens showing live security camera feeds of a store"></div>

    <footer class="contact-bar">
      <span class="contact">
        <svg viewBox="0 0 16 16"><circle cx="8" cy="8" r="7" fill="none" stroke="#fff" stroke-width="1.3"/><path d="M5.5 4.5l1.5 1.5-1 1c.5 1.2 1.3 2 2.5 2.5l1-1 1.5 1.5-1 1C7.5 11 5 8.5 4.5 6z" fill="#fff"/></svg>1-800-555-0142</span>
      <span class="contact">
        <svg viewBox="0 0 16 16"><rect x="1.5" y="3.5" width="13" height="9" fill="none" stroke="#fff" stroke-width="1.3"/><path d="M1.5 3.5L8 9l6.5-5.5" fill="none" stroke="#fff" stroke-width="1.3"/></svg>sales@lookdepot.example</span>
      <span class="contact">
        <svg viewBox="0 0 16 16"><circle cx="8" cy="8" r="6.5" fill="none" stroke="#fff" stroke-width="1.3"/><path d="M1.5 8h13M8 1.5c-3 3.5-3 9.5 0 13M8 1.5c3 3.5 3 9.5 0 13" fill="none" stroke="#fff" stroke-width="1.1"/></svg>www.lookdepot.example</span>
    </footer>
  </section>
</main>
</body>
</html>
```